TIDAL VERGE needs bisness cards pronto

Bisness name is "TIDAL VERGE" new bisness the bisness includes lawn mowing, garden matanace, and any jobs around the house.
I need a card that is colorful and vibrant and the bisness of lawn mowing maybe with some nature with it. It also needs my contact details"Darren Quellby mobile 0413562049 call for free quote and email norma.vance@fernmail.com.au and a catchy tag line

Industry/Entity Type

House

Requirements
Must have
• Bisness name "TIDAL VERGE"
Contact details "0413562049"
Email norma.vance@fernmail.com.au
Call for free quote

```html
<!DOCTYPE html>
<html lang="en">
<head>
<meta charset="utf-8">
<title>Tidal Verge – Business Card</title>
<link rel="stylesheet" href="https://fonts.googleapis.com/css2?family=Quicksand:wght@600&family=Fira+Sans:wght@500;600;700&display=swap">
<style>
  :root {
    --page-bg: #f2f4f6;
    --sky-light: #e4f8fe;
    --sky-mid: #5fcbef;
    --sky-deep: #1596c9;
    --navy: #0d3e5c;
    --panel-top: #5a5a5c;
    --panel-bottom: #3a3a3c;
    --ribbon-light: #f0381c;
    --ribbon-dark: #b01205;
    --ribbon-fold: #7c0c02;
    --lime: #c4ef12;
    --white: #ffffff;
    --email: #35c4ea;
  }
  * { box-sizing: border-box; margin: 0; padding: 0; }
  html, body {
    width: 1200px;
    height: 1000px;
    overflow: hidden;
    background: var(--page-bg);
  }
  .business-card {
    position: absolute;
    left: 75px;
    top: 200px;
    width: 1050px;
    height: 600px;
    overflow: hidden;
    background:
      radial-gradient(ellipse 70% 85% at 88% 28%, var(--sky-light) 0%, var(--sky-mid) 45%, var(--sky-deep) 100%);
    box-shadow: 0 18px 40px rgba(0, 0, 0, 0.18);
  }
  .brand-name {
    position: absolute;
    left: 70px;
    top: 36px;
    font-family: "Fira Sans", sans-serif;
    font-weight: 700;
    font-size: 84px;
    line-height: 96px;
    letter-spacing: 8px;
    color: var(--navy);
    white-space: nowrap;
  }
  .tagline {
    position: absolute;
    left: 72px;
    top: 134px;
    font-family: "Quicksand", sans-serif;
    font-weight: 600;
    font-size: 26px;
    letter-spacing: 0.5px;
    color: var(--navy);
    white-space: nowrap;
  }
  .contact-panel {
    position: absolute;
    left: 153px;
    top: 204px;
    width: 740px;
    height: 420px;
    border-radius: 26px 26px 0 0;
    background: linear-gradient(180deg, var(--panel-top), var(--panel-bottom));
    box-shadow: 0 -2px 10px rgba(0, 0, 0, 0.25);
  }
  .quote-call {
    position: absolute;
    left: 153px;
    width: 740px;
    top: 226px;
    text-align: center;
    font-family: "Fira Sans", sans-serif;
    font-weight: 600;
    font-size: 23px;
    color: var(--lime);
  }
  .phone-ribbon {
    position: absolute;
    left: 110px;
    top: 262px;
    width: 800px;
    height: 116px;
  }
  .phone-number {
    position: absolute;
    left: 110px;
    top: 268px;
    width: 775px;
    text-align: center;
    font-family: "Fira Sans", sans-serif;
    font-weight: 700;
    font-size: 76px;
    letter-spacing: 4px;
    line-height: 90px;
    color: var(--white);
  }
  .owner-name {
    position: absolute;
    left: 153px;
    width: 740px;
    top: 390px;
    text-align: center;
    font-family: "Fira Sans", sans-serif;
    font-weight: 500;
    font-size: 36px;
    color: var(--white);
  }
  .email {
    position: absolute;
    left: 153px;
    width: 740px;
    top: 455px;
    text-align: center;
    font-family: "Fira Sans", sans-serif;
    font-weight: 500;
    font-size: 30px;
    letter-spacing: 2px;
    color: var(--email);
  }
</style>
</head>
<body>
  <div class="business-card">
    <div class="brand-name">TIDAL VERGE</div>
    <div class="tagline">lawn mowing | garden maintenance | any jobs around the house</div>

    <div class="contact-panel"></div>
    <div class="quote-call">Call for FREE quote</div>

    <svg class="phone-ribbon" viewBox="0 0 800 116" aria-hidden="true">
      <defs>
        <linearGradient id="ribbonFace" x1="0" y1="0" x2="0" y2="1">
          <stop offset="0" stop-color="#f0381c"/>
          <stop offset="1" stop-color="#b01205"/>
        </linearGradient>
      </defs>
      <polygon points="0,18 775,4 775,92 0,104" fill="url(#ribbonFace)"/>
      <polygon points="775,4 800,26 800,100 775,92" fill="#7c0c02"/>
      <polygon points="0,104 12,116 12,104" fill="#7c0c02"/>
    </svg>
    <div class="phone-number">0413562049</div>

    <div class="owner-name">Darren Quellby</div>
    <div class="email">norma.vance@fernmail.com.au</div>
  </div>
</body>
</html>
```